Website for an electrical contractor :)

We are after a web site which can show pictures of our jobs and our capability in a professional, creative and easily understood way.

----- Brightmoor Electrical ------

We really want a visually good looking website with three sections

Section one:
'Completed projects'
We have a few pictures of jobs which we've completed and would like to show off with a brief description. (see uploads)

Section two:
'Our capabilities'
Just a list of what services we offer

Section three:
We would like a 'contact us' section which people can send us a short msg and upload a file for plans to be able to send to us. We would need their name, phone number and email details. We would also need a short privacy policy saying 'we do not disclose information to third parties'.
We also want to display our contact number and postal address

Good luck :)

Target Market(s)

Adults 25 years+
Business owners
Builders
Real estate agents

Industry/Entity Type

Electrical

Colors

Designer to choose colors to be used in the design.

Requirements
Must have
• Visually appealing
Easy to understand
In the 'Completed projects' section, must have a list for each project we do i can upload pictures for it.

```html
<!DOCTYPE html>
<html lang="en">
<head>
<meta charset="utf-8">
<title>Brightmoor Electrical</title>
<link href="https://fonts.googleapis.com/css2?family=Signika:wght@400;600&family=Open+Sans:wght@400;600;700&display=swap" rel="stylesheet">
<style>
:root{
  --red:#e11b22;
  --dark:#111111;
  --nav:#5a5a5a;
  --grey-bg:#eeeeee;
  --text:#333333;
  --muted:#777777;
  --light:#f6f6f6;
}
*{margin:0;padding:0;box-sizing:border-box}
html,body{width:768px;height:1200px;overflow:hidden;background:#fff}
body{position:relative;font-family:'Open Sans',sans-serif;color:var(--text)}
.abs{position:absolute}
.header{left:0;top:0;width:768px;height:57px;background:#f1f1f1}
.brand{left:103px;top:12px;display:flex;align-items:center;gap:6px}
.brand-dot{width:16px;height:16px;border-radius:50%;background:var(--red)}
.brand-name{font-family:'Signika',sans-serif;font-size:25px;color:#555;line-height:1}
.brand-sub{font-size:4.5px;color:#777;left:139px;top:40px;letter-spacing:.2px}
.phone{left:580px;top:11px;font-family:'Signika',sans-serif;font-weight:600;font-size:11.5px;color:#222}
.phone-btn{left:651px;top:10px;width:14px;height:14px;background:var(--red);border-radius:2px}
.search{left:535px;top:29px;width:111px;height:17px;background:#fff;font-size:5.5px;color:#999;padding:5px 9px}
.search-btn{left:646px;top:29px;width:19px;height:17px;background:var(--red)}
.nav{left:0;top:57px;width:768px;height:24px;background:var(--nav)}
.nav a{position:absolute;top:6px;font-size:7px;color:#fff;text-decoration:none}
.nav .active{left:103px;top:4px;width:48px;height:16px;background:var(--red);font-weight:700;text-align:center;padding-top:2px}
.soc{width:13px;height:13px;top:63px}
.hero{left:0;top:81px;width:768px;height:239px;background:linear-gradient(180deg,#8d8a82 0%,#bdb6a8 45%,#7e766a 100%)}
.hero-line{left:0;top:319px;width:768px;height:2px;background:var(--red)}
.tag{font-family:'Signika',sans-serif;font-weight:600;color:#fff;font-size:17px;text-align:center;line-height:28px}
.tag-red{left:317px;top:171px;width:134px;height:28px;background:var(--red)}
.tag-grey{left:341px;top:204px;width:110px;height:28px;background:#5d5d5d}
.amp{left:325px;top:210px;font-family:'Signika',sans-serif;font-size:13px;color:#222;font-weight:600}
.dots{left:360px;top:309px;width:48px;height:20px;background:var(--red);border-radius:4px 4px 0 0}
.section-title{width:768px;left:0;text-align:center;font-family:'Signika',sans-serif;font-size:15px}
.projects-title{top:346px;color:var(--red)}
.card-img{top:384px;width:130px;height:77px;border:1px solid #ddd;padding:3px;background:#fff}
.card-img div{width:100%;height:100%}
.card-title{top:468px;font-family:'Signika',sans-serif;font-size:9px;color:#333}
.card-text{top:486px;width:130px;font-size:5.2px;line-height:8.8px;color:var(--muted)}
.btn{top:520px;width:48px;height:19px;font-size:5.5px;font-weight:700;color:#fff;background:var(--red);text-align:center;line-height:19px}
.capabilities{left:0;top:562px;width:768px;height:436px;background:var(--grey-bg)}
.cap-title{top:581px;color:#333}
.cap-img{top:616px;height:172px;border:1px solid #d6d6d6;padding:5px;background:#fff}
.cap-img div{width:100%;height:100%}
.cap-head{top:800px;font-family:'Signika',sans-serif;font-size:12px;color:#333}
.list{list-style:none;top:823px;font-size:5.4px;font-weight:600;color:#333}
.list li{height:14.4px;line-height:8px;padding-left:8px;position:relative}
.list li::before{content:"";position:absolute;left:0;top:3px;width:3px;height:3px;background:#444}
.list li.hl{background:var(--red);color:#fff;width:129px;height:9px;margin-bottom:5.4px}
.list li.hl::before{background:#fff}
.footer{left:0;top:998px;width:768px;height:176px;background:var(--dark)}
.foot-brand-name{font-family:'Signika',sans-serif;font-size:25px;color:#666}
.foot-text{left:103px;top:1068px;width:130px;font-size:5.2px;line-height:8.8px;color:#666}
.foot-head{font-family:'Signika',sans-serif;font-size:13px;color:var(--red);font-weight:600}
.info{font-size:6.3px;color:#777;display:flex;gap:7px;align-items:flex-start}
.info svg{flex:none;margin-top:1px}
.field{left:487px;width:178px;height:14px;background:#222;font-size:5px;color:#666;padding:3px 4px}
.fbtn{top:1145px;width:82px;height:19px;font-size:6.5px;font-weight:700;text-align:center;line-height:17px}
.bottom{left:0;top:1174px;width:768px;height:26px;background:var(--dark);border-top:1px solid var(--red)}
.copy{left:104px;top:1183px;font-size:4.8px;color:var(--red)}
</style>
</head>
<body>

<header class="abs header"></header>
<div class="abs brand"><span class="brand-dot"></span><span class="brand-name">Brightmoor</span></div>
<div class="abs brand-sub">Electrical &amp; Communications · EC1234</div>
<div class="abs phone">04 5550 1827</div>
<div class="abs phone-btn"><svg width="14" height="14" viewBox="0 0 14 14"><path d="M5 4l1.3 1.5-.7 1a4 4 0 0 0 1.9 1.9l1-.7L10 9l-.6 1A5 5 0 0 1 4 4.6z" fill="#fff"/></svg></div>
<div class="abs search">Search here...</div>
<div class="abs search-btn"><svg width="19" height="17" viewBox="0 0 19 17"><circle cx="9" cy="8" r="2.6" fill="none" stroke="#fff" stroke-width="1.2"/><path d="M11 10l2 2" stroke="#fff" stroke-width="1.3"/></svg></div>

<nav class="abs nav">
  <a class="active">Home</a>
  <a style="left:173px">About Us</a>
  <a style="left:236px">Our Projects</a>
  <a style="left:310px">Our Capabilities</a>
  <a style="left:395px">Blog</a>
  <a style="left:444px">Contact Us</a>
</nav>
<div class="abs soc" style="left:612px;background:var(--red)"></div>
<div class="abs soc" style="left:631px;background:#777"></div>
<div class="abs soc" style="left:650px;background:#777"></div>

<div class="abs hero" role="img" aria-label="Finished interior of a function room with lounge seating, windows and double doors"></div>
<div class="abs hero-line"></div>
<div class="abs tag tag-red">Development</div>
<div class="abs amp">&amp;</div>
<div class="abs tag tag-grey">Installation</div>
<div class="abs dots"><svg width="48" height="20" viewBox="0 0 48 20"><circle cx="12" cy="11" r="3.3" fill="none" stroke="#fff"/><circle cx="24" cy="11" r="3.6" fill="#fff"/><circle cx="36" cy="11" r="3.3" fill="none" stroke="#fff"/></svg></div>

<h2 class="abs section-title projects-title">Our Projects</h2>

<div class="abs card-img" style="left:103px"><div role="img" aria-label="Kitchen project photo" style="background:linear-gradient(160deg,#e59a9a,#c65a5c)"></div></div>
<div class="abs card-img" style="left:247px"><div role="img" aria-label="Function room project photo" style="background:linear-gradient(180deg,#6f6a63,#b9b3a6 60%,#5f5a54)"></div></div>
<div class="abs card-img" style="left:391px"><div role="img" aria-label="Lounge room project photo" style="background:linear-gradient(180deg,#9f9a91,#cfc9be 60%,#8e887f)"></div></div>
<div class="abs card-img" style="left:535px"><div role="img" aria-label="Warehouse construction project photo" style="background:linear-gradient(180deg,#4a4d50,#7f8378 60%,#a79f86)"></div></div>

<div class="abs card-title" style="left:103px;color:var(--red)">Lorem Ipsum is simply dummy</div>
<div class="abs card-title" style="left:247px">Lorem Ipsum is simply dummy</div>
<div class="abs card-title" style="left:391px">Lorem Ipsum is simply dummy</div>
<div class="abs card-title" style="left:535px">Lorem Ipsum is simply dummy</div>

<p class="abs card-text" style="left:103px">Lorem Ipsum is simply dummy text of the printing and typesetting industry. Lorem Ipsum has been the industry</p>
<p class="abs card-text" style="left:247px">Lorem Ipsum is simply dummy text of the printing and typesetting industry. Lorem Ipsum has been the industry</p>
<p class="abs card-text" style="left:391px">Lorem Ipsum is simply dummy text of the printing and typesetting industry. Lorem Ipsum has been the industry</p>
<p class="abs card-text" style="left:535px">Lorem Ipsum is simply dummy text of the printing and typesetting industry. Lorem Ipsum has been the industry</p>

<div class="abs btn" style="left:103px;background:var(--dark)">Read More</div>
<div class="abs btn" style="left:247px">Read More</div>
<div class="abs btn" style="left:391px">Read More</div>
<div class="abs btn" style="left:535px">Read More</div>

<section class="abs capabilities"></section>
<h2 class="abs section-title cap-title">Our Capabilities</h2>
<div class="abs cap-img" style="left:103px;width:273px"><div role="img" aria-label="Residential townhouses with paved driveway" style="background:linear-gradient(180deg,#2f6fcf 0%,#86a9d8 40%,#5b5b58 65%,#8a8276 100%)"></div></div>
<div class="abs cap-img" style="left:391px;width:274px"><div role="img" aria-label="Two-storey concrete commercial building under construction" style="background:linear-gradient(180deg,#1f4fb0 0%,#4d7fd0 35%,#cfcac0 55%,#b8b2a6 100%)"></div></div>

<h3 class="abs cap-head" style="left:103px">Residential Capability Statement</h3>
<h3 class="abs cap-head" style="left:391px">Commercial / Industrial Capability Statement</h3>

<ul class="abs list" style="left:104px">
  <li class="hl">24hr Support / faults</li><li>Mains/sub mains cabling</li><li>RCD (Safety Switch) installations</li><li>Smoke alarms</li><li>Power points</li><li>Lighting points</li><li>External lighting</li><li>Sensor lighting</li><li>Switching</li><li>Antennas and Arial points</li><li>Dimmers</li>
</ul>
<ul class="abs list" style="left:247px">
  <li>Ceiling fans</li><li>Exhaust fans</li><li>Kitchen / Bathroom Projects</li><li>Re-wires</li><li>Smart wiring</li><li>Phone points</li><li>Data points</li><li>Switchboard installations/relocations</li><li>Compliance investigations/inspections</li><li>Concrete and wall chasing</li><li>Temporary builders site power</li>
</ul>
<ul class="abs list" style="left:391px">
  <li>24hr Support / faults</li><li>Lighting/power design and consultation</li><li>Emergency and exit lighting</li><li>Led strip lighting</li><li>Energy efficient lighting</li><li>Temporary lighting</li><li>Illuminated signage</li><li>Switchboard relocations</li><li>Maintenance</li><li>RCD installation</li>
</ul>
<ul class="abs list" style="left:535px">
  <li>Phone/data points</li><li>Data cabinets</li><li>Data Networking</li><li>IDF installations/relocations</li><li>All power requirements</li><li>All three phase power requirements</li><li>Electrical rip outs / Disconnections</li><li>Thermal Imaging scans</li><li>Commercial lighting</li><li>Concrete and wall chasing</li>
</ul>

<footer class="abs footer"></footer>
<div class="abs brand" style="top:1024px"><span class="brand-dot" style="background:#666"></span><span class="foot-brand-name">Brightmoor</span></div>
<div class="abs brand-sub" style="top:1051px;color:#666">Electrical &amp; Communications · EC1234</div>
<p class="abs foot-text">Lorem Ipsum is simply dummy text of the printing and typesetting industry. Lorem Ipsum has been the industry's standard dummy text ever since</p>
<div class="abs foot-head" style="left:103px;top:1111px">Follow Us On</div>
<div class="abs" style="left:103px;top:1140px;width:14px;height:14px;border-radius:50%;background:#2b5cab"></div>
<div class="abs" style="left:123px;top:1140px;width:14px;height:14px;border-radius:50%;background:#3a3a3a"></div>
<div class="abs" style="left:143px;top:1140px;width:14px;height:14px;border-radius:50%;background:#3a3a3a"></div>

<div class="abs foot-head" style="left:295px;top:1019px">Contact Info</div>
<div class="abs info" style="left:295px;top:1045px"><svg width="6" height="7" viewBox="0 0 6 7"><path d="M1 0l1.3 1.6-.6.9a3 3 0 0 0 1.8 1.8l.9-.6L6 5l-.6 1.2A4.6 4.6 0 0 1 0 .7z" fill="#666"/></svg>04 5550 1827</div>
<div class="abs info" style="left:295px;top:1060px"><svg width="6" height="7" viewBox="0 0 6 7"><rect x="0" y="2" width="6" height="4" fill="#666"/><rect x="1.3" y="0" width="3.4" height="2.4" fill="#666"/></svg>08 5550 3419</div>
<div class="abs info" style="left:295px;top:1075px"><svg width="6" height="7" viewBox="0 0 6 7"><rect x="0" y="1.5" width="6" height="4.5" fill="#666"/><path d="M0 1.7l3 2.2 3-2.2" fill="none" stroke="#222" stroke-width=".6"/></svg>info@brightmoorelectrical.com.au</div>
<div class="abs info" style="left:295px;top:1092px;line-height:9.5px"><svg width="6" height="8" viewBox="0 0 6 8"><path d="M3 8L.5 4A2.6 2.6 0 1 1 5.5 4z" fill="#666"/><circle cx="3" cy="2.7" r=".9" fill="#111"/></svg><span>P.O Box 410 Harbour Point W.A<br>6999 A.B.N: 12 345 678 901</span></div>

<div class="abs foot-head" style="left:487px;top:1019px">Contact From</div>
<div class="abs field" style="top:1047px">Enter Your Name :</div>
<div class="abs field" style="top:1067px">Enter Your Phone :</div>
<div class="abs field" style="top:1086px">Enter Your Email :</div>
<div class="abs field" style="top:1106px;height:33px">Massage :</div>
<div class="abs fbtn" style="left:487px;border:1px solid #ccc;color:#fff;background:#111">Upload File</div>
<div class="abs fbtn" style="left:583px;background:var(--red);color:#fff;line-height:19px">Submit</div>

<div class="abs bottom"></div>
<div class="abs copy">All Copyrights Reserved © Brightmoor Electrical 2015. Privacy Policy</div>

</body>
</html>
```